Architecture firm needing a business card

We need a business card design for a new company based in the US called "Pellmore Architecture". Seeking minimalist designs that have a creativity/design feel but must be clean and professional. Please refer to the logo attached.

Target Market(s)

Real Estate Investors, Home Builders and Construction Firms.

Industry/Entity Type

Architecture

Contact Information for Business Card

Standard US size business cards. Would like to have some sort of graphic on the back side of the card - nothing that is too loud but something that may catch your attention. More or less grayscale colors that are in line with the logo colors (navy and greys essentially). Additional colors maybe accepted if blended properly (earthtones), but might be difficult to accomplish and maintain the clean/minimalist look.

Requirements
Must have
• Clean Lines
Nice to have
• some sort of graphics, would like to have something creative on the back side of the card
Should not have
• nothing too busy, cluttered or overwhelming.

```html
<!DOCTYPE html>
<html lang="en">
<head>
<meta charset="utf-8">
<title>Pellmore Architecture – Business Card</title>
<link href="https://fonts.googleapis.com/css2?family=Nunito+Sans:wght@400;600&display=swap" rel="stylesheet">
<style>
  :root {
    --backdrop: #e7e4df;
    --card-white: #ffffff;
    --navy: #1d3e63;
    --navy-text: #1f3a5c;
    --grey-text: #8a8d91;
    --logo-grey: #9a9b9d;
    --divider: #d9d9d9;
  }
  * { margin: 0; padding: 0; box-sizing: border-box; }
  html, body {
    width: 1200px; height: 1000px; overflow: hidden;
    background: var(--backdrop);
    font-family: "Nunito Sans", "Avenir", sans-serif;
  }
  .canvas { position: relative; width: 1200px; height: 1000px; }

  .card {
    position: absolute; left: 265px; width: 666px; height: 397px;
    box-shadow: 0 3px 8px rgba(0,0,0,0.25);
  }
  .card--front { top: 73px; background: var(--card-white); }
  .card--back  { top: 532px; background: var(--navy); }

  .wordmark {
    position: absolute; display: flex; align-items: center; gap: 12px;
    font-weight: 400; letter-spacing: 0.06em; text-transform: uppercase; line-height: 1.05;
  }
  .wordmark__square { display: block; flex: none; }
  .wordmark__name { display: flex; flex-direction: column; }

  .card--front .wordmark { left: 38px; top: 166px; color: var(--navy-text); font-size: 31px; }
  .card--front .wordmark__square { width: 46px; height: 46px; background: var(--navy); }

  .card--back .wordmark { left: 132px; top: 156px; color: #ffffff; font-size: 46px; }
  .card--back .wordmark__square { width: 70px; height: 70px; background: #ffffff; }

  .divider {
    position: absolute; left: 358px; top: 82px; width: 2px; height: 248px;
    background: linear-gradient(to bottom, rgba(0,0,0,0), var(--divider) 30%, var(--divider) 70%, rgba(0,0,0,0));
  }

  .details { position: absolute; left: 400px; top: 84px; color: var(--grey-text); font-size: 17px; line-height: 24px; }
  .details__name { color: var(--navy-text); font-size: 22px; font-weight: 600; line-height: 26px; }
  .details__role { margin-bottom: 22px; }
  .details__address { margin-bottom: 8px; }
  .contact-list { list-style: none; }
  .contact-list li { display: flex; align-items: center; gap: 7px; height: 24.5px; }
  .contact-list svg { width: 15px; height: 15px; fill: var(--navy-text); flex: none; }
</style>
</head>
<body>
<div class="canvas">

  <section class="card card--front">
    <div class="wordmark">
      <span class="wordmark__square"></span>
      <span class="wordmark__name"><span>Pellmore</span><span>Architecture</span></span>
    </div>
    <div class="divider"></div>
    <div class="details">
      <p class="details__name">Daniel Whitford</p>
      <p class="details__role">Chef Executive Officer</p>
      <p class="details__address">48 N. Larkin Av, Suite 310<br>Brookvale, CA 90412</p>
      <ul class="contact-list">
        <li>
          <svg viewBox="0 0 16 16" aria-hidden="true"><path d="M3.5 1.5l2.2-.4 1.4 3.3-1.5 1.1a8 8 0 0 0 4.9 4.9l1.1-1.5 3.3 1.4-.4 2.2c-.2.9-1 1.5-1.9 1.4C6.9 13.4 2.6 9.1 2.1 3.4c-.1-.9.5-1.7 1.4-1.9z"/></svg>
          <span>+ 000 000 0000</span>
        </li>
        <li>
          <svg viewBox="0 0 16 16" aria-hidden="true"><rect x="4" y="1.5" width="8" height="4"/><rect x="1" y="6" width="14" height="6" rx="1"/><rect x="4" y="10" width="8" height="4.5" fill="#fff"/><rect x="5" y="11" width="6" height="3.5"/></svg>
          <span>+ 000 000 0000</span>
        </li>
        <li>
          <svg viewBox="0 0 16 16" aria-hidden="true"><rect x="1" y="3" width="14" height="10"/><path d="M1.5 3.5L8 9l6.5-5.5" fill="none" stroke="#fff" stroke-width="1.3"/></svg>
          <span>info@pellmorearch.com</span>
        </li>
        <li>
          <svg viewBox="0 0 16 16" aria-hidden="true"><circle cx="8" cy="8" r="7"/><path d="M1 8h14M8 1c-3 3.5-3 10.5 0 14M8 1c3 3.5 3 10.5 0 14" fill="none" stroke="#fff" stroke-width="1"/></svg>
          <span>www.pellmorearch.com</span>
        </li>
      </ul>
    </div>
  </section>

  <section class="card card--back">
    <div class="wordmark">
      <span class="wordmark__square"></span>
      <span class="wordmark__name"><span>Pellmore</span><span>Architecture</span></span>
    </div>
  </section>

</div>
</body>
</html>
```